Real Estate Investor needs awesome business card design

I invest in real estate, focused on multi-family properties, and I need a business card to hand out to potential partners. I prefer simple, clean designs, but it needs to stand out, so I'd like there to be a bit of red in the design as well.

It should include this information:

Front
Dallin Pecksworth
Real Estate Investor
Direct phone: 502-867-3394
Email: dallinhpecksworth@quillmail.example
Headshot (Picture), I've uploaded a few, just pick the one you think looks best with your design. You can remove the background from the headshot image if it looks better.

Back
The back of the card's design should flow and be congruent with the front. On the back I want to put an inspirational quote or question. There will be different ones depending on the card, so I'll need the original file so I can edit it in the end.

For now, use “The Pessimist Sees Difficulty In Every Opportunity. The Optimist Sees The Opportunity In Every Difficulty.” -Barnaby Ellsworth

Target Market(s)

Investors

Industry/Entity Type

Real Estate

Contact Information for Business Card

Front
Dallin Pecksworth
Real Estate Investor

Back
The back of the card's design should flow and be congruent with the front. On the back I want to put an inspirational quote or question. There will be different ones depending on the card, so I'll need the original file so I can edit it in the end. I've uploaded some EXAMPLES of business cards with quotes on them. Don't copy but feel free to use them as inspiration.

The design will be printed on "ZIB sized" business cards
1039 x 697 pixels
with rounded corners

Font styles to use
Serif
Decorative
Script

Colors
ec1f27

Requirements
Must have
• Headshot, name, and other information in it.
• 1039 x 697 pixels
• Rounded corners
• Clean design that pops. I'm open to see any color background, including black.
• Headshots can be located here: https://www.filecrate.example/sh/8kd2wq7mzt31hvx/BBQTXP4ruf9LmQ0KhcvWx7b?dl=0
Nice to have
• It would be awesome if the design included a personal signature or monogram, but if not I'll get a personal logo developed later and the card redesigned if I think it needs it.
Should not have
• Cluttered design

```html
<!DOCTYPE html>
<html lang="en">
<head>
<meta charset="utf-8">
<title>Dallin Pecksworth – Business Card</title>
<link rel="stylesheet" href="https://fonts.googleapis.com/css2?family=PT+Serif:wght@400;700&family=Big+Shoulders+Stencil+Display:wght@800&family=Great+Vibes&display=swap">
<style>
  :root {
    --page-bg: #eceeed;
    --card-black: #050506;
    --card-grey: #4d4e50;
    --text-white: #ffffff;
    --accent-red: #a8212a;
    --photo-light: #a9a9aa;
    --photo-mid: #5c5c5e;
    --photo-dark: #1e1e1f;
  }
  html, body {
    margin: 0;
    padding: 0;
    overflow: hidden;
  }
  body {
    width: 1047px;
    height: 1200px;
    background: var(--page-bg);
    position: relative;
  }
  .card {
    position: absolute;
    width: 717px;
    height: 432px;
    border-radius: 38px;
    overflow: hidden;
    color: var(--text-white);
  }
  .card--front {
    left: 167px;
    top: 124px;
    background: radial-gradient(ellipse 420px 360px at 230px 180px, var(--card-grey) 0%, #1c1c1d 60%, var(--card-black) 100%);
  }
  .card--back {
    left: 165px;
    top: 610px;
    background: radial-gradient(ellipse 480px 400px at 510px 190px, #5a5b5d 0%, #222224 55%, var(--card-black) 100%);
  }
  .headshot {
    position: absolute;
    left: 0;
    top: 0;
    width: 455px;
    height: 432px;
    background: linear-gradient(180deg, var(--photo-light) 0%, var(--photo-mid) 55%, var(--photo-dark) 100%);
    -webkit-mask-image: linear-gradient(90deg, #000 0%, #000 62%, transparent 100%);
    mask-image: linear-gradient(90deg, #000 0%, #000 62%, transparent 100%);
  }
  .identity {
    position: absolute;
    right: 64px;
    top: 121px;
    text-align: right;
    font-family: "PT Serif", serif;
  }
  .identity__name {
    margin: 0;
    font-size: 25px;
    font-weight: 700;
    line-height: 1;
  }
  .identity__role {
    margin: 10px 0 0;
    font-size: 21px;
    font-weight: 400;
    word-spacing: 6px;
    line-height: 1;
  }
  .contact {
    list-style: none;
    margin: 42px 0 0;
    padding: 0;
    font-size: 19px;
    line-height: 1;
  }
  .contact__item {
    display: flex;
    justify-content: flex-end;
    align-items: center;
    gap: 6px;
    margin-bottom: 13px;
  }
  .contact__icon {
    flex: none;
  }
  .quote {
    position: absolute;
    left: 137px;
    top: 62px;
    margin: 0;
    font-family: "Big Shoulders Stencil Display", sans-serif;
    font-weight: 800;
    font-size: 34px;
    line-height: 41px;
    letter-spacing: 0.6px;
    text-transform: uppercase;
  }
  .quote__line {
    display: block;
  }
  .quote__line--gap {
    margin-top: 5px;
  }
  .quote__accent {
    color: var(--accent-red);
  }
  .quote__mark {
    fill: var(--accent-red);
  }
  .quote__mark--open {
    position: absolute;
    left: -39px;
    top: 8px;
  }
  .quote__mark--close {
    margin-left: 5px;
    vertical-align: -2px;
  }
  .quote__author {
    position: absolute;
    right: 82px;
    top: 342px;
    margin: 0;
    font-family: "Great Vibes", cursive;
    font-size: 24px;
  }
</style>
</head>
<body>
  <section class="card card--front" aria-label="Business card front">
    <div class="headshot" role="img" aria-label="Black and white headshot of Dallin Pecksworth in a dark suit and white shirt"></div>
    <div class="identity">
      <h1 class="identity__name">DALLIN PECKSWORTH</h1>
      <p class="identity__role">Real Estate Investor</p>
      <ul class="contact">
        <li class="contact__item">
          <svg class="contact__icon" width="16" height="22" viewBox="0 0 16 22" aria-hidden="true">
            <rect x="1.5" y="1" width="13" height="20" rx="2" fill="none" stroke="#fff" stroke-width="1.6"/>
            <line x1="1.5" y1="16.5" x2="14.5" y2="16.5" stroke="#fff" stroke-width="1.4"/>
          </svg>
          <span>502-867-3394</span>
        </li>
        <li class="contact__item">
          <svg class="contact__icon" width="22" height="15" viewBox="0 0 22 15" aria-hidden="true">
            <rect x="1" y="1" width="20" height="13" rx="1" fill="none" stroke="#fff" stroke-width="1.6"/>
            <polyline points="1,1 11,9 21,1" fill="none" stroke="#fff" stroke-width="1.5"/>
            <line x1="1" y1="14" x2="8" y2="7" stroke="#fff" stroke-width="1.3"/>
            <line x1="21" y1="14" x2="14" y2="7" stroke="#fff" stroke-width="1.3"/>
          </svg>
          <span>dallinhpecksworth@quillmail.example</span>
        </li>
      </ul>
    </div>
  </section>

  <section class="card card--back" aria-label="Business card back">
    <blockquote class="quote">
      <svg class="quote__mark quote__mark--open" width="30" height="27" viewBox="0 0 30 27" aria-hidden="true">
        <polygon points="10,0 16,0 7,13.5 16,27 10,27 1,13.5"/>
        <polygon points="23,0 29,0 20,13.5 29,27 23,27 14,13.5"/>
      </svg>
      <span class="quote__line">The pessimist sees</span>
      <span class="quote__line">difficulty</span>
      <span class="quote__line quote__line--gap">In every <span class="quote__accent">opportunity.</span></span>
      <span class="quote__line">The optimist sees</span>
      <span class="quote__line quote__accent">The opportunity</span>
      <span class="quote__line">In every difficulty.<svg class="quote__mark quote__mark--close" width="30" height="27" viewBox="0 0 30 27" aria-hidden="true">
        <polygon points="1,0 7,0 16,13.5 7,27 1,27 10,13.5"/>
        <polygon points="14,0 20,0 29,13.5 20,27 14,27 23,13.5"/>
      </svg></span>
    </blockquote>
    <p class="quote__author">Barnaby Ellsworth</p>
  </section>
</body>
</html>
```